Home Page Design

We are refreshing our website and need someone to design a very clean modern home page. We have a wireframe for the content and basic layout (see attached). We just need someone to make it look beautiful.

This web page will be hosted on a private server using HTML5. I have developers who will integrate the rotating images and referenced video files - we just need you to focus on the visual elements.

You can take a look at our current website at tavenfold.com for color style guides, logos, etc.

```html
<!DOCTYPE html>
<html lang="en">
<head>
<meta charset="utf-8">
<title>Tavenfold – Home</title>
<link href="https://fonts.googleapis.com/css2?family=Ubuntu:wght@400;500;700&display=swap" rel="stylesheet">
<style>
:root{
  --blue:#27a9e1;
  --green:#8cc63f;
  --green-tint:#eef4e6;
  --navy:#1c2b45;
  --ink:#222a33;
  --text:#4a525a;
  --muted:#9aa2aa;
  --hero-bg:#f1f2f3;
  --white:#ffffff;
}
*{box-sizing:border-box;margin:0;padding:0}
html,body{width:1200px;height:1200px;overflow:hidden;background:var(--white)}
body{font-family:"Ubuntu",sans-serif;color:var(--text)}
.page{position:absolute;left:375px;top:0;width:563px;height:1500px;transform:scale(.8);transform-origin:0 0;background:var(--white)}
.abs{position:absolute}

.topbar{left:217px;top:0;width:346px;height:14px;background:var(--blue);border-bottom-left-radius:8px;color:var(--white);font-size:4.5px;display:flex;align-items:center;padding:0 0 0 35px}
.topbar a{color:inherit;text-decoration:none;margin-right:8px}
.topbar .phone{margin-left:auto;margin-right:76px}
.brand{left:76px;top:14px;font-size:13px;font-weight:500;color:var(--blue);display:flex;align-items:center;gap:3px}
.brand i{width:6px;height:6px;border-radius:50%;background:var(--blue)}
.mainnav{left:292px;top:23px;font-size:4.8px;color:var(--ink);display:flex;gap:9px}
.btn-cta{left:392px;top:21px;width:52px;height:10px;background:var(--green);color:var(--white);font-size:4.5px;display:flex;align-items:center;justify-content:center}
.btn-login{left:452px;top:21px;width:35px;height:10px;border:1px solid var(--green);color:var(--green);font-size:4.5px;display:flex;align-items:center;justify-content:center}

.hero{left:0;top:37px;width:563px;height:207px;background:linear-gradient(90deg,var(--hero-bg) 0%,#f6f6f6 40%,#c9ccd0 60%,#6d6257 100%)}
.hero-photo{left:230px;top:37px;width:333px;height:207px;background:linear-gradient(120deg,#e4e6e8 0%,#8d959c 40%,#3f4550 70%,#7a5e46 100%);opacity:.85}
.hero h1{left:76px;top:90px;font-size:16.5px;font-weight:500;color:var(--ink);letter-spacing:.2px}
.hero-title{left:76px;top:90px;font-size:16.5px;font-weight:500;color:var(--ink)}
.hero-title span{color:var(--blue)}
.hero-sub{left:76px;top:111px;font-size:9.5px;color:var(--ink);letter-spacing:.3px}
.stat{top:141px;width:59px;height:36px;background:var(--white);box-shadow:0 1px 4px rgba(0,0,0,.12);text-align:center;font-size:4px;color:var(--ink);padding-top:5px;line-height:1.45}
.stat b{display:block;color:var(--green);font-size:6.5px;font-weight:500}
.stat em{font-style:normal;color:var(--blue)}

.tab{top:231px;width:94px;height:35px;background:var(--white);box-shadow:0 1px 5px rgba(0,0,0,.12);display:flex;align-items:center;gap:10px;padding-left:11px;font-size:4.8px;color:var(--blue);line-height:1.6;text-transform:uppercase}
.tab svg{width:18px;height:16px;stroke:var(--navy);fill:none;stroke-width:1.3}
.tab.active{background:var(--blue);color:var(--white)}
.tab.active svg{stroke:var(--white)}

.section-title{font-size:9.5px;color:var(--blue);letter-spacing:.6px;text-transform:uppercase}
.bullets{list-style:none;font-size:4.8px;color:var(--ink)}
.bullets li{height:13.6px;position:relative;padding-left:7px}
.bullets li::before{content:"";position:absolute;left:0;top:1.5px;width:2px;height:2px;border-radius:50%;background:var(--blue)}
.more{width:20px;height:10px;background:var(--green-tint)}
.more svg{position:absolute;left:0;top:2px;width:18px;height:6px;stroke:var(--green);fill:none;stroke-width:1}
.frame{background:var(--green-tint)}
.photo{box-shadow:0 2px 8px rgba(0,0,0,.18)}

.testimonial{left:0;top:922px;width:563px;height:209px;background:var(--blue)}
.monitor{left:106px;top:950px;width:190px;height:230px;border-radius:4px;background:linear-gradient(160deg,#1d2329 0%,#0b0f13 55%,#d5d8db 78%,#f0f1f2 100%)}
.t-title{left:322px;top:957px;font-size:9.5px;color:var(--white);letter-spacing:.6px}
.avatar{left:322px;top:981px;width:32px;height:27px;background:linear-gradient(135deg,#d9a88a,#6e4a3a)}
.t-name{left:362px;top:981px;font-size:5px;color:var(--white)}
.t-name span{color:#bfe6f7;font-style:italic;margin-left:3px}
.t-stars{left:362px;top:989px;font-size:5.5px;color:var(--white);letter-spacing:.6px}
.t-quote{left:362px;top:997px;font-size:3.6px;color:var(--white)}
.t-body{left:322px;top:1016px;width:162px;font-size:4.2px;line-height:9.8px;color:var(--white);font-weight:500}
.t-nav{left:322px;top:1092px;display:flex;gap:4px}
.t-nav svg{width:14px;height:8px;stroke:var(--white);fill:none;stroke-width:1}
.t-nav .next{width:20px;height:10px;background:rgba(255,255,255,.3);display:flex;align-items:center;justify-content:center}

.fa-sub{left:75px;top:1222px;font-size:4.8px;color:var(--green);font-weight:500}
.fa-body{left:75px;top:1234px;width:168px;font-size:4.4px;line-height:9.9px;color:var(--ink)}

.footer{left:0;top:1382px;width:563px;height:118px;background:var(--navy);color:var(--white)}
.f-col{top:16px;font-size:4.6px;line-height:12px}
.f-col h4{font-size:5px;font-weight:500}
.f-brand{left:357px;top:16px;font-size:8px;font-weight:500}
.f-contact{left:357px;top:31px;font-size:4.4px;line-height:10.5px;font-weight:500}
.f-bottom{top:94px;font-size:3.8px;color:#c7ceda}
.f-social{left:434px;top:101px;display:flex;align-items:center;gap:3px;font-size:3.8px}
.f-social i{width:5px;height:5px;background:var(--white);border-radius:1px;display:inline-block}
</style>
</head>
<body>
<div class="page">

  <header>
    <nav class="abs topbar"><a>About Us</a><a>Contact</a><a>Support</a><a>Partners</a><span class="phone">+1 (800) 555-0142</span></nav>
    <div class="abs brand">tavenfold<i></i></div>
    <nav class="abs mainnav"><span>SOLUTIONS</span><span>PRICING</span><span>FAQS</span></nav>
    <a class="abs btn-cta">FREE ASSESMENT</a>
    <a class="abs btn-login">LOGIN</a>
  </header>

  <section>
    <div class="abs hero"></div>
    <div class="abs hero-photo" role="img" aria-label="Hands typing on a laptop showing cost charts beside a coffee cup"></div>
    <div class="abs hero-title">THE <span>ULTIMATE</span> CLOUD</div>
    <div class="abs hero-sub">Cost Optimization Solutions</div>
    <div class="abs stat" style="left:76px">Average Reduction<b>47%</b>TOTAL <em>CLOUD</em> SPEND</div>
    <div class="abs stat" style="left:146px">Average Cash ROI<b>501x</b>FIRST <em>YEAR</em></div>

    <div class="abs tab" style="left:76px"><svg viewBox="0 0 18 16"><rect x="1" y="1" width="5" height="4"/><rect x="12" y="1" width="5" height="4"/><rect x="1" y="11" width="5" height="4"/><rect x="12" y="11" width="5" height="4"/><path d="M3.5 5v6M14.5 5v6M6 3h6"/></svg><span>NextGen<br>Technology</span></div>
    <div class="abs tab active" style="left:182px"><svg viewBox="0 0 18 16"><rect x="1" y="1" width="5" height="4"/><rect x="12" y="1" width="5" height="4"/><rect x="1" y="11" width="5" height="4"/><rect x="12" y="11" width="5" height="4"/><path d="M3.5 5v6M14.5 5v6M6 13h6"/></svg><span>Advanced<br>Cost Analytics</span></div>
    <div class="abs tab" style="left:287px"><svg viewBox="0 0 18 16"><rect x="1" y="1" width="5" height="4"/><rect x="12" y="1" width="5" height="4"/><rect x="1" y="11" width="5" height="4"/><rect x="12" y="11" width="5" height="4"/><path d="M3.5 5v6M14.5 5v6M6 3l6 10"/></svg><span>Managed<br>Services</span></div>
    <div class="abs tab" style="left:393px"><svg viewBox="0 0 18 16"><rect x="1" y="1" width="5" height="4"/><rect x="12" y="1" width="5" height="4"/><rect x="1" y="11" width="5" height="4"/><rect x="12" y="11" width="5" height="4"/><path d="M3.5 5v6M14.5 5v6M6 13l6-10"/></svg><span>Certified Cloud<br>Engineers</span></div>
  </section>

  <section>
    <div class="abs" style="left:109px;top:293px;width:167px;height:169px;background:linear-gradient(180deg,#eceef0,#d7dadd);border-radius:10px" role="img" aria-label="Three phones showing a report library app"></div>
    <h2 class="abs section-title" style="left:322px;top:314px">NextGen Technology</h2>
    <ul class="abs bullets" style="left:322px;top:339px">
      <li>Lorem ipsum dolor sit amet, consectetur adipiscing elit.</li><li>Aliquam auctor porta semper.</li><li>Curabitur id lacinia ex.</li><li>Ut congue lacus ligula.</li><li>Suspendisse mollis nulla sit amet tincidunt pellentesque.</li><li>Quisque commodo lobortis vestibulum.</li><li>In blandit sit amet odio feugiat imperdiet.</li><li>Maecenas a arcu euismod, dignissim orci ut, interdum sem.</li>
    </ul>
    <div class="abs more" style="left:322px;top:454px"><svg viewBox="0 0 18 6"><path d="M0 3h16M13 1l3 2-3 2"/></svg></div>
  </section>

  <section>
    <h2 class="abs section-title" style="left:75px;top:520px">Advanced Cost Analytics</h2>
    <ul class="abs bullets" style="left:75px;top:545px">
      <li>Lorem ipsum dolor sit amet, consectetur adipiscing elit.</li><li>Aliquam auctor porta semper.</li><li>Curabitur id lacinia ex.</li><li>Ut congue lacus ligula.</li><li>Suspendisse mollis nulla sit amet tincidunt pellentesque.</li><li>Quisque commodo lobortis vestibulum.</li><li>In blandit sit amet odio feugiat imperdiet.</li><li>Maecenas a arcu euismod, dignissim orci ut, interdum sem.</li>
    </ul>
    <div class="abs more" style="left:75px;top:659px"><svg viewBox="0 0 18 6"><path d="M0 3h16M13 1l3 2-3 2"/></svg></div>
    <div class="abs frame" style="left:293px;top:540px;width:175px;height:126px"></div>
    <div class="abs photo" style="left:308px;top:521px;width:176px;height:127px;background:linear-gradient(135deg,#3d4249,#8a8f94 55%,#d8d4cf)" role="img" aria-label="Hands typing on a silver laptop"></div>
  </section>

  <section>
    <div class="abs frame" style="left:83px;top:735px;width:185px;height:127px"></div>
    <div class="abs photo" style="left:98px;top:717px;width:177px;height:126px;background:linear-gradient(135deg,#2b2f36,#6c7077 50%,#e6e7e9)" role="img" aria-label="Woman in glasses working at a computer desk"></div>
    <h2 class="abs section-title" style="left:322px;top:716px">Managed Services</h2>
    <ul class="abs bullets" style="left:322px;top:740px">
      <li>Lorem ipsum dolor sit amet, consectetur adipiscing elit.</li><li>Aliquam auctor porta semper.</li><li>Curabitur id lacinia ex.</li><li>Ut congue lacus ligula.</li><li>Suspendisse mollis nulla sit amet tincidunt pellentesque.</li><li>Quisque commodo lobortis vestibulum.</li><li>In blandit sit amet odio feugiat imperdiet.</li><li>Maecenas a arcu euismod, dignissim orci ut, interdum sem.</li>
    </ul>
    <div class="abs more" style="left:322px;top:855px"><svg viewBox="0 0 18 6"><path d="M0 3h16M13 1l3 2-3 2"/></svg></div>
  </section>

  <section>
    <div class="abs testimonial"></div>
    <div class="abs monitor" role="img" aria-label="Desktop monitor showing a dark cloud network diagram"></div>
    <h2 class="abs t-title">LISTEN TO OUR CUSTOMERS</h2>
    <div class="abs avatar" role="img" aria-label="Customer portrait"></div>
    <div class="abs t-name">Mara Hollis<span>Cloud Engineer</span></div>
    <div class="abs t-stars">★★★★★</div>
    <div class="abs t-quote">"USING TAVENFOLD IS A NO BRAINER"</div>
    <p class="abs t-body">Lorem ipsum dolor sit amet, consectetur adipiscing elit. Nulla sit amet nisl ac sem molestie cursus eget non diam. Nunc sed quam neque. Duis varius est eget arcu suscipit fringilla. Aliquam eu egestas sem, vitae scelerisque justo. Cras auctor urna neque, non malesuada tortor laoreet a. Phasellus mollis velit nec nisl faucibus pellentesque.</p>
    <div class="abs t-nav"><svg viewBox="0 0 14 8"><path d="M14 4H1M4 1L1 4l3 3"/></svg><span class="next"><svg viewBox="0 0 14 8"><path d="M0 4h13M10 1l3 3-3 3"/></svg></span></div>
  </section>

  <section>
    <h2 class="abs section-title" style="left:75px;top:1203px">Free Assesment</h2>
    <div class="abs fa-sub">No Risk * real cost savings estimate</div>
    <p class="abs fa-body">Lorem ipsum dolor sit amet, consectetur adipiscing elit. Nulla sit amet nisl ac sem molestie cursus eget non diam. Nunc sed quam neque. Duis varius est eget arcu suscipit fringilla. Aliquam eu egestas sem, vitae scelerisque justo. Cras auctor urna neque, non malesuada tortor laoreet a. Nulla pretium sodales tortor eget porttitor. Duis lorem ligula, consectetur in ornare et, congue quis erat. Integer libero tortor.</p>
    <div class="abs more" style="left:75px;top:1342px"><svg viewBox="0 0 18 6"><path d="M0 3h16M13 1l3 2-3 2"/></svg></div>
    <div class="abs frame" style="left:293px;top:1222px;width:175px;height:127px"></div>
    <div class="abs photo" style="left:308px;top:1205px;width:176px;height:125px;background:linear-gradient(135deg,#1e2126,#52585e 45%,#dfe1e3)" role="img" aria-label="Desktop computer on a desk with a plant and coffee cup"></div>
  </section>

  <footer class="abs footer">
    <div class="abs f-col" style="left:75px"><h4>Company</h4>About Us<br>Contact Us</div>
    <div class="abs f-col" style="left:145px"><h4>Products</h4>Solutions<br>Features<br>Pricing<br>FAQ</div>
    <div class="abs f-col" style="left:216px"><h4>Customers</h4>Sales<br>Supports</div>
    <div class="abs f-col" style="left:286px"><h4>Partners</h4>Become a Reseller<br>Portal Login</div>
    <div class="abs f-brand">tavenfold</div>
    <div class="abs f-contact">240 Harbor Lane, Millbrook, OH 44000<br>Email : sales@tavenfold.com<br>Phone : +1 (800) 555-0142</div>
    <div class="abs f-bottom" style="left:76px">Policy | Terms &amp; condition | Site map</div>
    <div class="abs f-bottom" style="left:240px;top:96px">© 2016 Tavenfold , All rights reserved</div>
    <div class="abs f-social">Follow Us | <i></i><i></i><i></i></div>
  </footer>

</div>
</body>
</html>
```